Business card design needed

I need a business card for my private practice. I would like to see the designs that use bright blue and white. I would like to see similar designs as to the card below:
http://blog.printmoss.com/2009/designing-a-business-card-with-pm-kt517-template.html
I would like to see the back of the card have room for appointment times. Thank you.

Industry/Entity Type
Business
Contact Information for Business Card
Tandem Wellbeing & Guidance Services
Fiona Marsh B.Psychology
Registered Psychologist
Building C, Level 3, 14 Wattle Crescent, Canberra, ACT 2601
T: (02) 6248 7315
F: (02) 6248 7390
info@tandemwellbeing.com.au
www.tandemwellbeing.com.au

```html
<!DOCTYPE html>
<html lang="en">
<head>
<meta charset="utf-8">
<title>Tandem Wellbeing &amp; Guidance Services – Business Card</title>
<link href="https://fonts.googleapis.com/css2?family=Open+Sans:wght@400;600&display=swap" rel="stylesheet">
<style>
  :root {
    --backdrop: #2b2b2b;
    --card: #ffffff;
    --card-shade: #f1f2f3;
    --blue: #1e9ccb;
    --blue-deep: #1688b5;
    --blue-light: #8fd3ec;
    --blue-pale: #c4e8f5;
  }
  * { box-sizing: border-box; margin: 0; padding: 0; }
  html, body {
    width: 1200px; height: 900px; overflow: hidden;
    background: var(--backdrop);
    font-family: "Open Sans", Verdana, sans-serif;
  }
  .canvas { position: relative; width: 1200px; height: 900px; }

  .card {
    position: absolute; width: 560px; height: 320px;
    background: linear-gradient(135deg, var(--card) 0%, var(--card-shade) 100%);
    box-shadow: 0 18px 40px rgba(0,0,0,.55);
    overflow: hidden;
  }

  /* Front */
  .card--front { left: 80px; top: 90px; }
  .front-band {
    position: absolute; inset: 0;
    background: linear-gradient(90deg, var(--blue-light) 0%, var(--blue-pale) 30%, rgba(196,232,245,0) 48%);
  }
  .front-text {
    position: absolute; left: 250px; top: 92px;
    color: var(--blue); line-height: 1.15;
  }
  .front-text .practice {
    font-size: 19px; text-transform: uppercase; letter-spacing: .3px;
  }
  .front-text .person {
    margin-top: 4px; font-size: 17px; text-transform: uppercase;
  }
  .front-text .role { font-size: 14px; color: var(--blue-light); }

  /* Back */
  .card--back { left: 560px; top: 490px; }
  .appointments {
    position: absolute; left: 28px; top: 42px; width: 330px;
  }
  .appointments .label {
    color: var(--blue); font-size: 13px; text-transform: uppercase; letter-spacing: .5px;
  }
  .appointments .rule { height: 1px; background: var(--blue); margin-top: 16px; }
  .appointments .rule:first-child { margin-top: 0; }
  .rules { margin-top: -34px; margin-left: 0; }
  .rule-set { position: absolute; left: 28px; top: 18px; width: 340px; }
  .rule-set .rule { height: 1px; background: var(--blue); margin-bottom: 17px; }

  .website {
    position: absolute; left: 70px; top: 120px;
    color: var(--blue-deep); font-size: 15px; font-weight: 600; letter-spacing: .4px;
  }

  .brand {
    position: absolute; right: 30px; top: 70px;
    display: flex; align-items: center; gap: 10px;
  }
  .brand .dot {
    width: 22px; height: 22px; border-radius: 50%; background: var(--blue);
    flex: none;
  }
  .brand .name {
    color: var(--blue-deep); font-size: 11px; text-transform: uppercase; line-height: 1.2;
  }

  .contact {
    position: absolute; left: 30px; bottom: 26px;
    list-style: none; color: var(--blue-deep); font-size: 11.5px; line-height: 1.25;
  }
  .contact li { display: flex; align-items: flex-start; gap: 8px; margin-top: 5px; }
  .contact svg { flex: none; width: 15px; height: 15px; margin-top: 1px; }
</style>
</head>
<body>
<main class="canvas">

  <section class="card card--front" aria-label="Card front">
    <div class="front-band"></div>
    <div class="front-text">
      <p class="practice">Tandem Wellbeing<br>&amp; Guidance Services</p>
      <p class="person">Fiona Marsh B.</p>
      <p class="role">Psychology<br>Registered Psychologist</p>
    </div>
  </section>

  <section class="card card--back" aria-label="Card back">
    <div class="rule-set">
      <div class="rule"></div>
      <div class="rule" style="margin-bottom:4px"></div>
      <p class="appointments-label" style="color:var(--blue);font-size:13px;letter-spacing:.5px;margin-bottom:6px">APPOINTMENTS:</p>
      <div class="rule"></div>
      <div class="rule"></div>
    </div>
    <p class="website">www.tandemwellbeing.com.au</p>

    <div class="brand">
      <span class="dot"></span>
      <p class="name">Tandem Wellbeing<br>&amp; Guidance Services</p>
    </div>

    <ul class="contact">
      <li>
        <svg viewBox="0 0 16 16" aria-hidden="true"><circle cx="8" cy="8" r="7.5" fill="#1688b5"/><path d="M4 8.5 8 5l4 3.5M5.3 7.6V11h5.4V7.6" fill="none" stroke="#fff" stroke-width="1.3"/></svg>
        <span>Building C, Level 3, 14 Wattle Crescent,<br>Canberra, ACT 2601</span>
      </li>
      <li>
        <svg viewBox="0 0 16 16" aria-hidden="true"><circle cx="8" cy="8" r="7.5" fill="#1688b5"/><path d="M5.5 4.5c-.8.8-.6 2.6 1.3 4.6s3.8 2.2 4.6 1.4l-1.3-1.3-1 .6c-.8-.4-1.6-1.2-2-2l.6-1z" fill="#fff"/></svg>
        <span>(02) 6248 7315<br>(02) 6248 7390</span>
      </li>
      <li>
        <svg viewBox="0 0 16 16" aria-hidden="true"><circle cx="8" cy="8" r="7.5" fill="#1688b5"/><rect x="4" y="5.5" width="8" height="5" fill="#fff"/><path d="M4 5.5 8 8.5l4-3" fill="none" stroke="#1688b5" stroke-width=".9"/></svg>
        <span>info@tandemwellbeing.com.au</span>
      </li>
    </ul>
  </section>

</main>
</body>
</html>
```